Signboard menu for a Fastfood takeaway shop

My current signboard menu is old now, I want to upgrade to a new, bigger and brighter signboard menu.
Photos of the old menu attached but there are some changes in each sections of the menu needs to be changed.
Size of the signboard :
L: 1700cm
H: 1200cm

Industry/Entity Type

Fastfood Hospitality

Colors
FFC000
F8CF3A
FAE287
FDF2CF
FEFAEE

```html
<!DOCTYPE html>
<html lang="en">
<head>
<meta charset="utf-8">
<title>Takeaway Menu Board</title>
<link rel="stylesheet" href="https://fonts.googleapis.com/css2?family=Archivo+Black&family=Quicksand:wght@600;700&display=swap">
<style>
  :root {
    --board-red: #f25457;
    --board-red-deep: #e64548;
    --head-yellow: #f6e24a;
    --price-yellow: #f8d93a;
    --ink-white: #fff6ee;
    --rule-white: #fbe9e4;
    --art-tone: #f7a39a;
    --page-bg: #1c1612;
  }
  * { box-sizing: border-box; margin: 0; padding: 0; }
  html, body { width: 1200px; height: 800px; overflow: hidden; background: var(--page-bg); }
  .board {
    width: 1200px; height: 800px;
    background: var(--board-red);
    display: grid;
    grid-template-columns: 1fr 1fr 1fr;
    column-gap: 34px;
    padding: 22px 26px 18px;
    font-family: "Quicksand", sans-serif;
    font-weight: 700;
    color: var(--ink-white);
    text-transform: uppercase;
    letter-spacing: 0.13em;
    font-size: 9.2px;
  }
  .column { display: flex; flex-direction: column; min-width: 0; }
  .section { position: relative; margin-bottom: 10px; --art-space: 0px; }
  .section-title {
    font-family: "Archivo Black", sans-serif;
    color: var(--head-yellow);
    font-size: 15px;
    letter-spacing: 0.03em;
    line-height: 1;
    padding: 14px 0 5px;
    border-bottom: 1.5px solid var(--rule-white);
    margin-bottom: 7px;
    margin-right: var(--art-space);
    white-space: nowrap;
  }
  .art {
    position: absolute; top: 0; right: 0;
    border-radius: 8px;
    background: linear-gradient(135deg, var(--art-tone), var(--board-red-deep));
  }
  .item { display: flex; align-items: flex-end; line-height: 1.25; margin-bottom: 4px; }
  .item .name { flex: 0 1 auto; }
  .item .lead { flex: 1 1 14px; border-bottom: 1px solid var(--rule-white); margin: 0 5px 3px; min-width: 14px; opacity: .8; }
  .item .price { color: var(--price-yellow); white-space: nowrap; }
  .pair { display: grid; grid-template-columns: 1fr 1fr; column-gap: 14px; }
  .note { color: var(--price-yellow); line-height: 1.6; margin-bottom: 6px; font-size: 8.6px; }
  .desc .name { max-width: 78%; line-height: 1.6; }
  .scene-art { margin: 18px auto 0; width: 300px; height: 90px; border-radius: 40px; background: linear-gradient(135deg, var(--art-tone), var(--board-red-deep)); }
</style>
</head>
<body>
<main class="board">

  <section class="column">
    <div class="section" style="--art-space:130px">
      <h2 class="section-title">Sandwiches:</h2>
      <div class="art" role="img" aria-label="Line drawing of a sub sandwich" style="width:120px;height:34px"></div>
      <div class="pair">
        <div>
          <div class="item"><span class="name">Yeast spread</span><span class="lead"></span><span class="price">$ 4.50</span></div>
          <div class="item"><span class="name">Cheese</span><span class="lead"></span><span class="price">$ 4.50</span></div>
          <div class="item"><span class="name">Tomato</span><span class="lead"></span><span class="price">$ 4.50</span></div>
          <div class="item"><span class="name">Salad</span><span class="lead"></span><span class="price">$ 7.00</span></div>
          <div class="item"><span class="name">Ham</span><span class="lead"></span><span class="price">$ 7.50</span></div>
          <div class="item"><span class="name">Chicken</span><span class="lead"></span><span class="price">$ 7.50</span></div>
          <div class="item"><span class="name">Roast beef</span><span class="lead"></span><span class="price">$ 7.50</span></div>
        </div>
        <div>
          <div class="item"><span class="name">Rissole</span><span class="lead"></span><span class="price">$ 7.50</span></div>
          <div class="item"><span class="name">Sausage</span><span class="lead"></span><span class="price">$ 7.00</span></div>
          <div class="item"><span class="name">Scallop</span><span class="lead"></span><span class="price">$ 6.00</span></div>
          <div class="item"><span class="name">Chip</span><span class="lead"></span><span class="price">$ 6.00</span></div>
          <div class="item"><span class="name">Bacon</span><span class="lead"></span><span class="price">$ 7.00</span></div>
          <div class="item"><span class="name">Bacon/egg</span><span class="lead"></span><span class="price">$ 7.00</span></div>
          <div class="item"><span class="name">Schnitzel</span><span class="lead"></span><span class="price">$ 8.50</span></div>
        </div>
      </div>
      <div class="item"><span class="name">Or create your own for $ roll</span><span class="lead"></span><span class="price">+$ 6.00</span></div>
    </div>

    <div class="section" style="--art-space:64px">
      <h2 class="section-title">Salads in tubs:</h2>
      <div class="art" role="img" aria-label="Line drawing of a salad bowl" style="width:56px;height:32px"></div>
      <div class="item"><span class="name">Plain salad</span><span class="lead"></span><span class="price">$ 7.50</span></div>
      <div class="item"><span class="name">Caesar salad tub</span><span class="lead"></span><span class="price">$ 10.00</span></div>
      <div class="item"><span class="name">Tomato/beetroot/onion/cucumber</span><span class="lead"></span><span class="price">$ 0.50</span></div>
      <div class="pair">
        <div>
          <div class="item"><span class="name">Bacon/ meat</span><span class="lead"></span><span class="price">$ 2.50</span></div>
          <div class="item"><span class="name">Egg</span><span class="lead"></span><span class="price">$ 1.50</span></div>
        </div>
        <div>
          <div class="item"><span class="name">Pineapple</span><span class="lead"></span><span class="price">$ 1.00</span></div>
          <div class="item"><span class="name">Sauce</span><span class="lead"></span><span class="price">$ 0.50</span></div>
        </div>
      </div>
      <div class="item"><span class="name">Kebab meat: chicken 100gr</span><span class="lead"></span><span class="price">$ 3.50</span></div>
      <div class="pair">
        <div class="item"><span class="name">Lamb 100gr</span><span class="lead"></span><span class="price">$ 4.50</span></div>
        <div class="item"><span class="name">Avocado/ cheese</span><span class="lead"></span><span class="price">$ 4.50</span></div>
      </div>
    </div>

    <div class="section">
      <h2 class="section-title">Burgers: (beef or chicken)</h2>
      <div class="pair">
        <div>
          <div class="item"><span class="name">Plain</span><span class="lead"></span><span class="price">$ 7.00</span></div>
          <div class="item"><span class="name">Works</span><span class="lead"></span><span class="price">$ 10.00</span></div>
          <div class="item"><span class="name">Cheese</span><span class="lead"></span><span class="price">$ 8.00</span></div>
        </div>
        <div>
          <div class="item"><span class="name">Bacon/ cheese</span><span class="lead"></span><span class="price">$ 9.00</span></div>
          <div class="item"><span class="name">Bacon/egg burger</span><span class="lead"></span><span class="price">$ 9.50</span></div>
          <div class="item"><span class="name">Mexican</span><span class="lead"></span><span class="price">$ 8.00</span></div>
        </div>
      </div>
      <div class="item"><span class="name">Schnitzel burgers: extra</span><span class="lead"></span><span class="price">$ 1.50</span></div>
      <div class="item"><span class="name">Hawaiian (works burger with pineapple)</span><span class="lead"></span><span class="price">$ 11.00</span></div>
      <div class="item desc"><span class="name">Mega (works burger with double meat, double bacon and egg)</span><span class="lead"></span><span class="price">$ 15.00</span></div>
    </div>

    <div class="section" style="--art-space:48px">
      <h2 class="section-title">Bacon/egg roll or wraps</h2>
      <div class="art" role="img" aria-label="Drawing of a filled wrap" style="width:40px;height:26px;top:6px"></div>
      <div class="item"><span class="name">Bacon/egg</span><span class="lead"></span><span class="price">$ 7.00</span></div>
      <div class="item"><span class="name">Bacon/egg/cheese</span><span class="lead"></span><span class="price">$ 8.20</span></div>
      <div class="item"><span class="name">Bacon/egg/cheese/onion</span><span class="lead"></span><span class="price">$ 9.20</span></div>
      <div class="item"><span class="name">Wraps: extra</span><span class="lead"></span><span class="price">$ 3.00</span></div>
    </div>

    <div class="section">
      <h2 class="section-title">Gravy rolls</h2>
      <div class="pair">
        <div>
          <div class="item"><span class="name">Slow cook beef</span><span class="lead"></span><span class="price">$ 8.50</span></div>
          <div class="item"><span class="name">Slow cook pork</span><span class="lead"></span><span class="price">$ 8.00</span></div>
          <div class="item"><span class="name">Rissole</span><span class="lead"></span><span class="price">$ 8.00</span></div>
        </div>
        <div>
          <div class="item"><span class="name">Sausage</span><span class="lead"></span><span class="price">$ 7.00</span></div>
          <div class="item"><span class="name">Schnitzel</span><span class="lead"></span><span class="price">$ 8.00</span></div>
          <div class="item"><span class="name">Chips</span><span class="lead"></span><span class="price">$ 6.50</span></div>
        </div>
      </div>
    </div>
  </section>

  <section class="column">
    <div class="section" style="--art-space:136px">
      <h2 class="section-title">Kebabs</h2>
      <div class="art" role="img" aria-label="Line drawing of a kebab skewer" style="width:126px;height:24px;top:6px"></div>
      <div class="pair">
        <div>
          <div class="item"><span class="name">Chicken</span><span class="lead"></span><span class="price">$ 12.50</span></div>
          <div class="item"><span class="name">Mix</span><span class="lead"></span><span class="price">$ 14.50</span></div>
        </div>
        <div class="item"><span class="name">Lamb</span><span class="lead"></span><span class="price">$ 14.50</span></div>
      </div>
    </div>

    <div class="section" style="--art-space:100px">
      <h2 class="section-title">Schnitzel wraps</h2>
      <div class="art" role="img" aria-label="Drawing of a schnitzel wrap" style="width:36px;height:28px;right:60px;top:4px"></div>
      <div class="item"><span class="name">Caesar</span><span class="lead"></span><span class="price">$ 12.00</span></div>
      <div class="item"><span class="name">Salad and cheese</span><span class="lead"></span><span class="price">$ 11.00</span></div>
      <div class="item desc"><span class="name">Works (with bacon, egg, cheese and all salad):</span><span class="lead"></span><span class="price">$ 14.50</span></div>
      <div class="item desc"><span class="name">Mexican (mexican spiced schnitzel with lettuce, tomato, spanish onion, cheese, sour cream and hot chilli sauce) :</span><span class="lead"></span><span class="price">$ 10.50</span></div>
      <div class="item desc"><span class="name">Hawaiian (with bacon, lettuce, tomato, pineapple, cheese with honey mustard)</span><span class="lead"></span><span class="price">$ 12.00</span></div>
    </div>

    <div class="section">
      <h2 class="section-title">Snack packs</h2>
      <p class="note">(Kebab meats with chips, spanish onions, cheese and sauce of your choice)</p>
      <div style="width:60%">
        <div class="item"><span class="name">Chips</span><span class="lead"></span><span class="price">$ 13.00</span></div>
        <div class="item"><span class="name">Mix</span><span class="lead"></span><span class="price">$ 15.00</span></div>
        <div class="item"><span class="name">Lamb</span><span class="lead"></span><span class="price">$ 15.00</span></div>
      </div>
    </div>

    <div class="section" style="--art-space:90px">
      <h2 class="section-title">Hot food</h2>
      <div class="art" role="img" aria-label="Line drawing of a steaming bowl" style="width:42px;height:32px;right:40px;top:-2px"></div>
      <div class="pair">
        <div>
          <div class="item"><span class="name">Scallop</span><span class="lead"></span><span class="price">$ 2.00</span></div>
          <div class="item"><span class="name">Dim sim</span><span class="lead"></span><span class="price">$ 2.00</span></div>
          <div class="item"><span class="name">Hash brown</span><span class="lead"></span><span class="price">$ 2.50</span></div>
          <div class="item"><span class="name">Sausage</span><span class="lead"></span><span class="price">$ 3.00</span></div>
          <div class="item"><span class="name">Corn jack</span><span class="lead"></span><span class="price">$ 3.50</span></div>
          <div class="item"><span class="name">Chicken stick</span><span class="lead"></span><span class="price">$ 3.70</span></div>
        </div>
        <div>
          <div class="item"><span class="name">Crunch roll</span><span class="lead"></span><span class="price">$ 3.50</span></div>
          <div class="item"><span class="name">Battered sav</span><span class="lead"></span><span class="price">$ 3.50</span></div>
          <div class="item"><span class="name">Dippy dog</span><span class="lead"></span><span class="price">$ 4.50</span></div>
          <div class="item"><span class="name">Mini chicken</span></div>
          <div class="item"><span class="name">Dim sim *6</span><span class="lead"></span><span class="price">$ 3.00</span></div>
        </div>
      </div>
    </div>

    <div class="section">
      <h2 class="section-title">Chips:</h2>
      <div class="art" role="img" aria-label="Drawing of a bowl of chips" style="width:46px;height:32px;right:120px;top:-4px"></div>
      <div class="item"><span class="name">Small</span><span class="lead"></span><span class="price">$ 4.00</span></div>
      <div class="item"><span class="name">Medium</span><span class="lead"></span><span class="price">$ 6.00</span></div>
      <div class="item"><span class="name">Large</span><span class="lead"></span><span class="price">$ 8.00</span></div>
      <div class="item"><span class="name">Add gravy: extra</span><span class="lead"></span><span class="price">$ 2.00</span></div>
    </div>
  </section>

  <section class="column">
    <div class="section" style="--art-space:48px">
      <h2 class="section-title">Big breaky (special)</h2>
      <div class="art" role="img" aria-label="Line drawing of a steaming coffee cup" style="width:38px;height:34px;top:0"></div>
      <div class="item desc"><span class="name">Bacon, 2x eggs, sausage, fried tomato, hashbrown and toast</span><span class="lead"></span><span class="price">$ 15.00</span></div>
      <div class="item"><span class="name">With a small coffee</span><span class="lead"></span><span class="price">$ 17.00</span></div>
    </div>

    <div class="section" style="--art-space:160px">
      <h2 class="section-title">Seafood</h2>
      <div class="art" role="img" aria-label="Line drawing of a crab" style="width:42px;height:32px;right:110px;top:0"></div>
      <div class="pair">
        <div>
          <div class="item"><span class="name">Calamari ring</span><span class="lead"></span><span class="price">$ 2.00</span></div>
          <div class="item"><span class="name">Cocktail fish</span><span class="lead"></span><span class="price">$ 2.50</span></div>
          <div class="item"><span class="name">Crab stick</span><span class="lead"></span><span class="price">$ 2.50</span></div>
        </div>
        <div>
          <div class="item"><span class="name">Prawn cutlet</span><span class="lead"></span><span class="price">$ 2.50</span></div>
          <div class="item"><span class="name">Fish cake</span><span class="lead"></span><span class="price">$ 3.50</span></div>
          <div class="item"><span class="name">Battered fish</span><span class="lead"></span><span class="price">$ 7.00</span></div>
        </div>
      </div>
    </div>

    <div class="section">
      <h2 class="section-title">Seafood pack</h2>
      <div class="item" style="margin-bottom:12px"><span class="name">#1: Traditional: battered fish &amp; chip:</span><span class="lead"></span><span class="price">$ 9.00</span></div>
      <div class="item" style="margin-bottom:12px"><span class="name">#2: Snacking pack: 3 cocktail fish &amp; chip</span><span class="lead"></span><span class="price">$ 9.00</span></div>
      <div class="item desc" style="margin-bottom:12px"><span class="name">#3: Fisherman basket (2 calamari ring, 2 prawn cutlet, 1 crabstick, 1 cocktail fish, chip &amp; 1 can of soft drink) :</span><span class="lead"></span><span class="price">$ 18.00</span></div>
      <div class="item desc"><span class="name">#4: Family feast (4 prawn cutlets, 4 calamari rings, 4 crabstick, 6 cocktail fish &amp; 1.25L bottle of soft drink) :</span><span class="lead"></span><span class="price">$ 40.00</span></div>
    </div>

    <div class="scene-art" role="img" aria-label="Line drawing of a fish on a plate with salad leaves and a glass of soft drink"></div>
  </section>

</main>
</body>
</html>
```